Tasman Curdworks Guild needs new business cards

We need new business cards designed and produced. We are likely to need other design work done for ads, flyers etc in future.

We would like to start with an initial business card.

The Tasman Curdworks Guild (TCG) is a membership-based not-for-profit organisation that looks after the interests of Australia's small to medium artisan cheesemakers, many of whom are also small-scale farmers. The design should be simple, using our logo, but also communicate our artisan cheese and small dairy farm focus.

The first card to be designed and produced is for me, Miriam Tolhurst. My details are:

Miriam Tolhurst
Secretary
Tasman Curdworks Guild (TCG)
http://www.curdworksguild.example
T +61452837190
E miriam.miriamtolhurst@mailbox.example

I have attached the TCG logo in jpg form. I have a higher resolution version available if needed.

Thank you!

Miriam

Miriam Tolhurst
Tasman Curdworks Guild
miriam.miriamtolhurst@mailbox.example
+61452837190

Sans Serif

• Logo (see attached file)

```html
<!DOCTYPE html>
<html lang="en">
<head>
<meta charset="utf-8">
<title>Tasman Curdworks Guild — Business Card</title>
<link rel="stylesheet" href="https://fonts.googleapis.com/css2?family=PT+Sans:wght@400;700&display=swap">
<style>
  :root {
    --backdrop: #e9e4dc;
    --cheese: #f3c25c;
    --cheese-deep: #eab246;
    --card-white: #f7f7f7;
    --divider: #4a3a2c;
    --ink: #3b2a1c;
    --brand-brown: #6a4a30;
  }
  * { box-sizing: border-box; margin: 0; padding: 0; }
  html, body {
    width: 1200px;
    height: 738px;
    overflow: hidden;
    background: var(--backdrop);
    font-family: "PT Sans", Arial, sans-serif;
  }
  .stage {
    width: 1200px;
    height: 738px;
    display: flex;
    align-items: center;
    justify-content: center;
  }
  .business-card {
    width: 900px;
    height: 514px;
    display: flex;
    box-shadow: 0 10px 30px rgba(60, 40, 20, 0.18);
  }
  .card-front {
    position: relative;
    width: 430px;
    color: var(--ink);
    overflow: hidden;
  }
  .cheese-texture {
    position: absolute;
    inset: 0;
    background: linear-gradient(160deg, var(--cheese) 0%, var(--cheese-deep) 100%);
  }
  .holder {
    position: absolute;
    left: 52px;
    top: 36px;
  }
  .holder-name {
    font-size: 30px;
    font-weight: 400;
    letter-spacing: 1px;
    text-transform: uppercase;
  }
  .holder-role {
    font-size: 19px;
    letter-spacing: 1px;
    text-transform: uppercase;
    margin-top: 2px;
    margin-left: 2px;
  }
  .contact {
    position: absolute;
    left: 40px;
    top: 322px;
    list-style: none;
    font-size: 20px;
    line-height: 30px;
  }
  .contact-phone { padding-left: 12px; }
  .divider {
    width: 4px;
    background: var(--divider);
  }
  .card-back {
    flex: 1;
    background: linear-gradient(135deg, #ffffff 0%, var(--card-white) 60%, #ececec 100%);
    display: flex;
    align-items: center;
    justify-content: center;
    gap: 22px;
    padding: 0 40px;
  }
  .brand-dot {
    width: 70px;
    height: 70px;
    border-radius: 50%;
    background: var(--cheese);
    flex: none;
  }
  .brand-name {
    color: var(--brand-brown);
    font-size: 30px;
    font-weight: 400;
    line-height: 1.1;
    width: 220px;
  }
</style>
</head>
<body>
  <main class="stage">
    <article class="business-card">
      <section class="card-front">
        <div class="cheese-texture" role="img" aria-label="Cheese-yellow panel with a scattered cheese-hole pattern"></div>
        <header class="holder">
          <h1 class="holder-name">Miriam Tolhurst</h1>
          <p class="holder-role">Secretary</p>
        </header>
        <ul class="contact">
          <li class="contact-phone">P : + 614 528 37190</li>
          <li class="contact-email">miriam.miriamtolhurst@mailbox.example</li>
          <li class="contact-web">www.curdworksguild.example</li>
        </ul>
      </section>
      <div class="divider"></div>
      <section class="card-back">
        <span class="brand-dot"></span>
        <p class="brand-name">Tasman Curdworks Guild</p>
      </section>
    </article>
  </main>
</body>
</html>
```